Trade Show Wall Graphic Design

We need a design for a poster/ graphic to be printed on the back wall of an industry exhibition.
Our business operates primarily in the Oil and Gas and Renewables industries.
We tend to prefer an infographic style.
Two of the companies within our group will be jointly exhibiting and the final design should demonstrate cohesion between the two while maintaining elements of the individual brand identities.

Requirements
Must have
• Stand dimensions:
• 1st wall - 5365mm x 2500mm
• 2nd Wall – 2395mm x 2500mm
• Both walls to have a 50mm bleed

```html
<!DOCTYPE html>
<html lang="en">
<head>
<meta charset="utf-8">
<title>Offshore Construction Services – Exhibition Wall</title>
<link href="https://fonts.googleapis.com/css2?family=Montserrat:wght@400;600;700;800&family=Open+Sans:wght@400;600&display=swap" rel="stylesheet">
<style>
:root{
  --navy:#12305e;
  --blue:#1f5fa8;
  --sky:#3f8fd2;
  --pale:#9fc6ea;
  --wall:#f4f5f7;
  --ink:#3b4656;
  --muted:#7d8794;
  --page:#e6e7ea;
}
*{box-sizing:border-box;margin:0;padding:0}
html,body{width:1200px;height:901px;overflow:hidden;background:var(--page)}
body{font-family:"Open Sans",sans-serif;color:var(--ink)}
.wall{position:absolute;left:20px;top:100px;width:1160px;height:700px;background:var(--wall);overflow:hidden}
.col{position:absolute;top:40px}
h1,h2,h3{font-family:"Montserrat",sans-serif;color:var(--navy)}
.intro{left:35px;width:200px}
.intro h1{font-size:19px;font-weight:800;line-height:1.2;text-transform:uppercase}
.offer-list{list-style:none;margin-top:14px}
.offer-list li{font-family:"Montserrat",sans-serif;font-size:15px;color:var(--blue);font-weight:600;margin-bottom:6px}
.offer-list li::before{content:"•";margin-right:8px;color:var(--sky)}
.stats{display:flex;gap:10px;margin-top:16px}
.stat{width:56px;height:56px;border-radius:50%;background:var(--blue);color:#fff;display:flex;align-items:center;justify-content:center;text-align:center;font-family:"Montserrat",sans-serif;font-size:9px;font-weight:700;line-height:1.15}
.stat:nth-child(2){background:var(--sky)}
.brand{margin-top:26px}
.brand-name{display:flex;align-items:center;gap:7px;font-family:"Montserrat",sans-serif;font-weight:800;font-size:15px;color:var(--navy);text-transform:uppercase;white-space:nowrap}
.brand-name .mark{width:14px;height:14px;background:var(--blue);border-radius:50%}
.brand-web{font-family:"Montserrat",sans-serif;font-size:13px;font-weight:700;color:var(--navy);margin-top:10px;white-space:nowrap}
.brand-tel{font-size:12px;color:var(--ink);margin-top:3px}
.brand + .brand{margin-top:30px}
.text-col h2{font-size:11px;font-weight:800;text-transform:uppercase;color:var(--blue);margin-bottom:8px}
.text-col p{font-size:8px;line-height:1.55;color:var(--muted);margin-bottom:8px}
.text-col h3{font-size:8.5px;font-weight:700;margin:6px 0 4px}
.text-col ul{list-style:none;margin-bottom:6px}
.text-col li{font-size:8px;color:var(--muted);line-height:1.6}
.text-col li::before{content:"›";color:var(--sky);margin-right:5px;font-weight:700}
.why{left:250px;width:200px}
.what{left:485px;width:215px}
.photo-cluster{position:absolute;left:255px;top:385px;width:465px;height:260px}
.photo{position:absolute;border-radius:50%;border:4px solid #fff;box-shadow:0 2px 6px rgba(0,0,0,.15)}
.p1{left:0;top:20px;width:110px;height:110px;background:radial-gradient(circle at 40% 40%,#f0b35a,#3a5f86)}
.p2{left:40px;top:135px;width:80px;height:80px;background:radial-gradient(circle at 50% 40%,#e9c04a,#5a7a44)}
.p3{left:140px;top:65px;width:150px;height:150px;background:radial-gradient(circle at 50% 35%,#f3d27a,#5e86b3)}
.p4{left:305px;top:10px;width:95px;height:95px;background:radial-gradient(circle at 40% 40%,#c7dff2,#2d5c92)}
.p5{left:375px;top:120px;width:85px;height:85px;background:radial-gradient(circle at 50% 45%,#f2a24a,#29496f)}
.presence{left:735px;width:400px}
.presence h2{font-size:16px;font-weight:800;text-transform:uppercase;color:var(--blue)}
.presence .lead{font-size:8px;color:var(--muted);margin-top:5px;width:300px}
.world-map{margin-top:10px;width:400px;height:230px;border-radius:4px;background:linear-gradient(135deg,#2a6fb9,#174a8a 60%,#12305e)}
.charts{display:grid;grid-template-columns:1fr 1fr;gap:14px 20px;margin-top:20px}
.chart{display:flex;align-items:center;gap:10px}
.chart svg{width:48px;height:48px;flex:none}
.chart-label{font-size:8.5px;color:var(--muted);line-height:1.35}
.chart-label b{display:block;font-family:"Montserrat",sans-serif;font-size:13px;color:var(--navy)}
.base-band{position:absolute;left:0;bottom:0;width:100%;height:44px}
.base-band .light{height:12px;background:var(--sky)}
.base-band .dark{height:32px;background:var(--navy)}
</style>
</head>
<body>
<main class="wall">

  <section class="col intro">
    <h1>Award Winning Offshore Construction Services</h1>
    <ul class="offer-list">
      <li>Oil and Gas</li>
      <li>Offshore Renewables</li>
      <li>Special Projects</li>
    </ul>
    <div class="stats">
      <div class="stat">25<br>Years</div>
      <div class="stat">400<br>Staff</div>
      <div class="stat">30<br>Countries</div>
    </div>
    <div class="brand">
      <div class="brand-name"><span class="mark"></span>Tideline Marine</div>
      <div class="brand-web">www.tidelinemarine.com</div>
      <div class="brand-tel">+44 (0)1224 000 111</div>
    </div>
    <div class="brand">
      <div class="brand-name"><span class="mark"></span>Corvane Subsea</div>
      <div class="brand-web">www.corvanesubsea.com</div>
      <div class="brand-tel">+44 (0)1224 000 222</div>
    </div>
  </section>

  <section class="col text-col why">
    <h2>Why Tideline</h2>
    <p>Tideline Marine brings decades of offshore know-how to every project, pairing seasoned crews with modern vessels to deliver safe, efficient construction from concept to handover.</p>
    <h3>Industries Served</h3>
    <ul>
      <li>Oil and Gas Platforms</li>
      <li>Offshore Wind Farms</li>
      <li>Subsea Pipelines</li>
      <li>Decommissioning</li>
    </ul>
    <h3>Core Strengths</h3>
    <ul>
      <li>Safety First Culture</li>
      <li>Certified Engineers</li>
      <li>Global Fleet Access</li>
    </ul>
  </section>

  <section class="col text-col what">
    <h2>What We Do</h2>
    <p>Corvane Subsea supports installation, inspection and repair across the full asset life, working hand in hand with Tideline Marine to offer one joined service.</p>
    <p>Together our teams cover planning, fabrication, lifting and marine logistics under one roof.</p>
    <h3>Services</h3>
    <ul>
      <li>Heavy Lift</li>
      <li>Cable Laying</li>
      <li>ROV Support</li>
      <li>Diving Teams</li>
    </ul>
    <h3>Engineering Solutions</h3>
    <ul>
      <li>Structural Design</li>
      <li>Project Management</li>
      <li>Marine Surveys</li>
    </ul>
  </section>

  <div class="photo-cluster">
    <div class="photo p1" role="img" aria-label="Offshore platform at sunset"></div>
    <div class="photo p2" role="img" aria-label="Construction equipment on deck"></div>
    <div class="photo p3" role="img" aria-label="Offshore crew in hard hats on site"></div>
    <div class="photo p4" role="img" aria-label="Offshore wind turbines at sea"></div>
    <div class="photo p5" role="img" aria-label="Construction vessel at dusk"></div>
  </div>

  <section class="col presence">
    <h2>Our Global Presence</h2>
    <p class="lead">With bases on four continents we mobilise quickly to projects wherever they are.</p>
    <div class="world-map" role="img" aria-label="World map in blue marking the group's office and project locations"></div>
    <div class="charts">
      <div class="chart">
        <svg viewBox="0 0 42 42"><circle cx="21" cy="21" r="15.9" fill="none" stroke="#d7e4f1" stroke-width="6"/><circle cx="21" cy="21" r="15.9" fill="none" stroke="#1f5fa8" stroke-width="6" stroke-dasharray="32 68" transform="rotate(-90 21 21)"/></svg>
        <div class="chart-label"><b>32%</b>Wind Projects</div>
      </div>
      <div class="chart">
        <svg viewBox="0 0 42 42"><circle cx="21" cy="21" r="15.9" fill="none" stroke="#d7e4f1" stroke-width="6"/><circle cx="21" cy="21" r="15.9" fill="none" stroke="#3f8fd2" stroke-width="6" stroke-dasharray="48 52" transform="rotate(-90 21 21)"/></svg>
        <div class="chart-label"><b>48%</b>Oil and Gas</div>
      </div>
      <div class="chart">
        <svg viewBox="0 0 42 42"><circle cx="21" cy="21" r="15.9" fill="none" stroke="#d7e4f1" stroke-width="6"/><circle cx="21" cy="21" r="15.9" fill="none" stroke="#12305e" stroke-width="6" stroke-dasharray="65 35" transform="rotate(-90 21 21)"/></svg>
        <div class="chart-label"><b>65%</b>Repeat Clients</div>
      </div>
      <div class="chart">
        <svg viewBox="0 0 42 42"><circle cx="21" cy="21" r="15.9" fill="none" stroke="#d7e4f1" stroke-width="6"/><circle cx="21" cy="21" r="15.9" fill="none" stroke="#1f5fa8" stroke-width="6" stroke-dasharray="20 80" transform="rotate(-90 21 21)"/></svg>
        <div class="chart-label"><b>20%</b>Special Projects</div>
      </div>
      <div class="chart">
        <svg viewBox="0 0 42 42"><circle cx="21" cy="21" r="15.9" fill="none" stroke="#d7e4f1" stroke-width="6"/><circle cx="21" cy="21" r="15.9" fill="none" stroke="#3f8fd2" stroke-width="6" stroke-dasharray="75 25" transform="rotate(-90 21 21)"/></svg>
        <div class="chart-label"><b>75%</b>Local Workforce</div>
      </div>
      <div class="chart">
        <svg viewBox="0 0 42 42"><circle cx="21" cy="21" r="15.9" fill="none" stroke="#d7e4f1" stroke-width="6"/><circle cx="21" cy="21" r="15.9" fill="none" stroke="#12305e" stroke-width="6" stroke-dasharray="90 10" transform="rotate(-90 21 21)"/></svg>
        <div class="chart-label"><b>90%</b>On Time Delivery</div>
      </div>
      <div class="chart">
        <svg viewBox="0 0 42 42"><circle cx="21" cy="21" r="15.9" fill="none" stroke="#d7e4f1" stroke-width="6"/><circle cx="21" cy="21" r="15.9" fill="none" stroke="#1f5fa8" stroke-width="6" stroke-dasharray="40 60" transform="rotate(-90 21 21)"/></svg>
        <div class="chart-label"><b>40%</b>Subsea Work</div>
      </div>
      <div class="chart">
        <svg viewBox="0 0 42 42"><circle cx="21" cy="21" r="15.9" fill="none" stroke="#d7e4f1" stroke-width="6"/><circle cx="21" cy="21" r="15.9" fill="none" stroke="#3f8fd2" stroke-width="6" stroke-dasharray="58 42" transform="rotate(-90 21 21)"/></svg>
        <div class="chart-label"><b>58%</b>Fleet Use Rate</div>
      </div>
    </div>
  </section>

  <div class="base-band"><div class="light"></div><div class="dark"></div></div>
</main>
</body>
</html>
```